Design a company business card

Design a business card based on our logo. Would like colors of the Philippine flag as the base design of the card. Using the attached color and Pantone. All entries who doesn’t comply to the color and design requirement will not be considered. I have attached our company logo. Company logo must be incorporated. A bit of information about our company, we are a Home Care Agency.

```html
<!DOCTYPE html>
<html lang="en">
<head>
<meta charset="utf-8">
<title>Kalinga Home Care Agency – Business Card</title>
<link href="https://fonts.googleapis.com/css2?family=Open+Sans:wght@400;600;800&display=swap" rel="stylesheet">
<style>
  :root {
    --stage: #2e3034;
    --flag-red: #d42027;
    --flag-blue: #1f3f9e;
    --flag-yellow: #f7c51e;
    --white: #ffffff;
    --card-w: 520px;
    --card-h: 310px;
  }
  * { box-sizing: border-box; margin: 0; padding: 0; }
  html, body {
    width: 1200px; height: 900px; overflow: hidden;
    background: var(--stage);
    font-family: "Open Sans", Arial, sans-serif;
  }
  .stage {
    position: relative; width: 1200px; height: 900px;
  }
  .card {
    position: absolute;
    width: var(--card-w); height: var(--card-h);
    border-radius: 28px;
    overflow: hidden;
  }
  .card--front { background: var(--flag-red); left: 640px; top: 250px; }
  .card--back  { background: var(--flag-blue); left: 40px; top: 340px; }

  .wordmark {
    display: flex; align-items: center; gap: 12px;
    font-weight: 800; letter-spacing: 0.5px; line-height: 1.05;
    text-transform: uppercase;
  }
  .wordmark__dot { border-radius: 50%; flex: none; }

  .card--front .wordmark {
    position: absolute; left: 0; right: 0; top: 0; bottom: 0;
    justify-content: center;
    color: var(--flag-blue); font-size: 30px;
  }
  .card--front .wordmark__dot { width: 34px; height: 34px; background: var(--flag-yellow); }

  .card--back .wordmark {
    position: absolute; left: 250px; top: 40px;
    color: var(--white); font-size: 20px;
  }
  .card--back .wordmark__dot { width: 24px; height: 24px; background: var(--flag-yellow); }

  .holder {
    position: absolute; left: 42px; top: 140px; width: 180px;
    color: var(--flag-yellow); text-align: right;
  }
  .holder__name { font-size: 21px; font-weight: 600; text-transform: uppercase; letter-spacing: 0.5px; }
  .holder__title { font-size: 11px; margin-top: 2px; }

  .divider {
    position: absolute; left: 238px; top: 128px;
    width: 2px; height: 90px; background: var(--flag-red);
  }

  .contacts {
    position: absolute; left: 256px; top: 122px;
    list-style: none; color: var(--white); font-size: 12.5px;
  }
  .contacts li { display: flex; align-items: center; gap: 8px; height: 19px; }
  .contacts svg { width: 12px; height: 12px; flex: none; }

  .address {
    position: absolute; left: 42px; bottom: 40px;
    color: var(--flag-red); font-size: 11.5px;
  }
</style>
</head>
<body>
<main class="stage">

  <section class="card card--back" aria-label="Business card, contact side">
    <div class="wordmark"><span class="wordmark__dot"></span><span>Kalinga<br>Home Care Agency</span></div>

    <div class="holder">
      <p class="holder__name">Marco Delgado</p>
      <p class="holder__title">CEO &amp; Founder</p>
    </div>

    <div class="divider"></div>

    <ul class="contacts">
      <li>
        <svg viewBox="0 0 12 12"><circle cx="6" cy="6" r="6" fill="#fff"/><path d="M4 3.2l1 1.2-.5.8c.4.8 1 1.4 1.8 1.8l.8-.5 1.2 1-.6 1c-2.3-.3-4-2-4.3-4.3z" fill="#1f3f9e"/></svg>
        555 210 0143
      </li>
      <li>
        <svg viewBox="0 0 12 12"><circle cx="6" cy="6" r="6" fill="#fff"/><rect x="4.2" y="2.6" width="3.6" height="6.8" rx="0.7" fill="#1f3f9e"/></svg>
        555 210 0144
      </li>
      <li>
        <svg viewBox="0 0 12 12"><circle cx="6" cy="6" r="6" fill="#fff"/><rect x="3" y="4" width="6" height="4.2" fill="#1f3f9e"/><path d="M3 4l3 2.3L9 4" stroke="#fff" stroke-width="0.7" fill="none"/></svg>
        hello@kalingacare.com
      </li>
      <li>
        <svg viewBox="0 0 12 12"><circle cx="6" cy="6" r="6" fill="#fff"/><circle cx="6" cy="6" r="3.2" fill="none" stroke="#1f3f9e" stroke-width="0.8"/><path d="M2.8 6h6.4M6 2.8v6.4" stroke="#1f3f9e" stroke-width="0.7"/></svg>
        www.kalingacare.com
      </li>
      <li>
        <svg viewBox="0 0 12 12"><circle cx="6" cy="6" r="6" fill="#fff"/></svg>
        @kalingahomecare
      </li>
    </ul>

    <p class="address">2 Mabini Street, Quezon City, Metro Manila, PH</p>
  </section>

  <section class="card card--front" aria-label="Business card, logo side">
    <div class="wordmark"><span class="wordmark__dot"></span><span>Kalinga<br>Home Care Agency</span></div>
  </section>

</main>
</body>
</html>
```